Granite Civic Builders Summit (GCBS) needs a flyer and logo design

We need a save the date flyer that can be easily edited to be a header only with event title, date and location.
We also are looking for a conference logo that will go well with our company logo.
Updates
Most of you are submitting an agenda design. Not a graphic flyer design. This isn't what I'm needing. I need something that can easily be a save the date with a header and is graphically appealing. Additionally, I've only gotten 2 logo designs.
Low design quality
Target Market(s)
Architects, engineers, public owners, contractors, attorneys
Industry/Entity Type
Construction
Logo Text
Granite Civic Builder's Summit
Requirements
Must have
- Flyer should Have:
- Title: "A Lantern Across Stormy Seas - Project Delivery to Operations”
- Date: August 8-9, 2019
- Location: Fort Worth, TX
- One-page only
- Conference Logo should be relatable to our company logo: Granite Civic Builders Summit.
Nice to have
- Topics:
- Alternative Constrcting: JOC & Design-Build
- Dealing with Contracting in a Tight TX Industry
- Tools & Technologies Project Delivery and Operations: Design and Construction
- Tools & Technologies: Coordinating Operations
Should not have
- Detailed agenda

```html
<!DOCTYPE html>
<html lang="en">
<head>
<meta charset="utf-8">
<title>Granite Civic Builders Summit – Save the Date</title>
<link rel="stylesheet" href="https://fonts.googleapis.com/css2?family=Bebas+Neue&family=Roboto:wght@700&display=swap">
<style>
  :root {
    --navy: #0b2447;
    --green: #3ab82e;
    --white: #ffffff;
    --gold: #f5b82e;
  }
  * { margin: 0; padding: 0; box-sizing: border-box; }
  html, body { width: 857px; height: 1200px; overflow: hidden; background: var(--white); }
  .flyer { position: relative; width: 857px; height: 1200px; background: var(--white); overflow: hidden; }
  .flyer-shapes { position: absolute; inset: 0; }
  .brand {
    position: absolute; left: 553px; top: 211px; width: 272px; height: 80px;
    display: flex; align-items: center; gap: 12px; padding-left: 10px;
  }
  .brand-mark { width: 22px; height: 22px; background: var(--green); flex: none; }
  .brand-name {
    font-family: 'Roboto', sans-serif; font-weight: 700; color: var(--navy);
    font-size: 17px; line-height: 1.15; text-transform: uppercase; letter-spacing: 0.5px;
  }
  .event-title {
    position: absolute; left: 40px; top: 458px; width: 720px;
    font-family: 'Bebas Neue', sans-serif; font-weight: 400; color: var(--white);
    font-size: 68px; line-height: 62px; letter-spacing: 2px; text-align: center;
  }
  .event-details {
    position: absolute; left: 39px; top: 818px;
    font-family: 'Roboto', sans-serif; font-weight: 700; color: var(--gold);
    font-size: 25px; line-height: 43px; letter-spacing: 1px;
  }
</style>
</head>
<body>
<main class="flyer">
  <svg class="flyer-shapes" width="857" height="1200" viewBox="0 0 857 1200" aria-hidden="true">
    <polygon class="corner-accent" points="0,0 598,0 250,179 0,303" fill="var(--green)"/>
    <polygon class="title-panel" points="0,303 250,179 857,414 857,1041 0,1041" fill="var(--navy)"/>
    <rect class="footer-band" x="0" y="1041" width="857" height="51" fill="var(--green)"/>
    <rect class="footer-band" x="0" y="1142" width="857" height="58" fill="var(--green)"/>
  </svg>

  <div class="brand">
    <span class="brand-mark"></span>
    <span class="brand-name">GCBS Granite Civic<br>Builders Summit</span>
  </div>

  <h1 class="event-title">"A Lantern Across Stormy Seas - Project Delivery to Operations”</h1>

  <p class="event-details">Date: August 8-9, 2019<br>Location: Fort Worth, TX</p>
</main>
</body>
</html>
```